Vemb - Website Design in WordPress (2 pages)

The goal of this design work is to create two highly focused, PPC- and SEO-aware landing pages that clearly explain the experience in familiar terms and drive app installs. The design must respect the existing visual identity and support future iteration of copy and content without requiring redesign.
Required Deliverables:
Fully working WordPress site containing:
Homepage template
Location landing page template
Mobile-first, responsive
CTA behaviour exactly as designed
Required
WordPress admin access
Full site export / backup
Homepage template
Mobile-first behaviour
CTA visible above the fold on mobile
Uses my:
Visual identity
Logo
Placeholder copy
I receive:
Admin access
Full site export / backup
Not acceptable
20+ plugins
Proprietary or abandoned builders
Hardcoded layouts that can’t be reused
Separate page designs per location
Elementor is preferred if:
One builder only
Clean structure
No custom lock-in widgets
Uploaded the mobile design for inspiration only
Coding
Coded - Design and coding required
Look and feel
Each slider illustrates characteristics of the customer's brand and the style your logo design should communicate.

```html
<!DOCTYPE html>
<html lang="en">
<head>
<meta charset="UTF-8">
<title>Vemb – Experience more of the world around you</title>
<link rel="stylesheet" href="https://fonts.googleapis.com/css2?family=Ubuntu:wght@400;500;700&display=swap">
<style>
  :root{
    --teal-deep:#0e6a76;
    --teal:#17808c;
    --teal-bright:#3ec0c8;
    --teal-soft:#d7f1f4;
    --teal-glow:#e8f7f9;
    --ink:#163a40;
    --muted:#4c6166;
    --band-a:#0d6a73;
    --band-b:#0a555c;
    --night:#0b2a31;
    --white:#ffffff;
    --line:#e3ecee;
  }
  *{box-sizing:border-box;margin:0;padding:0}
  html,body{width:1200px;height:3240px;overflow:hidden}
  body{font-family:"Ubuntu",Arial,sans-serif;color:var(--ink);background:var(--white);position:relative}

  /* hero */
  .hero{position:absolute;left:0;top:0;width:1200px;height:830px;overflow:hidden}
  .hero-circle{position:absolute;left:610px;top:-180px;width:860px;height:860px;border-radius:50%;
    background:radial-gradient(circle at 45% 55%,#5fd0d6 0%,#2bb0bb 45%,#1a95a1 100%)}
  .hero-ring{position:absolute;left:670px;top:-120px;width:740px;height:740px;border-radius:50%;border:2px solid rgba(255,255,255,.25)}
  .brand{position:absolute;left:112px;top:40px;font-weight:700;font-size:58px;color:var(--teal);letter-spacing:-1px}
  .hero-title{position:absolute;left:112px;top:222px;width:480px;font-size:40px;line-height:50px;font-weight:500;color:var(--teal);text-transform:uppercase;white-space:nowrap}
  .hero-title .accent{color:var(--teal-bright)}
  .hero-lead{position:absolute;left:112px;top:410px;width:440px;font-size:19px;line-height:28px;color:var(--ink)}
  .btn{display:inline-flex;align-items:center;justify-content:center;height:46px;padding:0 28px;border-radius:23px;font-size:16px;font-weight:500;color:var(--white);text-decoration:none;white-space:nowrap}
  .btn-dark{background:var(--teal-deep)}
  .btn-light{background:var(--teal-bright)}
  .btn-row{position:absolute;display:flex;gap:16px}
  .phone{position:absolute;border-radius:44px;border:10px solid #1d2326;box-shadow:0 20px 50px rgba(0,0,0,.25)}
  .phone-hero{left:722px;top:100px;width:280px;height:684px;background:linear-gradient(180deg,#2f4a4f 0%,#1d3538 40%,#0f2124 100%)}

  /* stats */
  .stats{position:absolute;left:0;top:850px;width:1200px;height:160px;border-bottom:1px solid var(--line)}
  .stat{position:absolute;top:20px}
  .stat b{display:block;font-size:62px;font-weight:400;color:var(--teal-deep);line-height:70px}
  .stat span{display:block;font-size:18px;color:var(--muted);margin-top:4px}

  /* features */
  .section-title{position:absolute;left:0;width:1200px;text-align:center;font-size:30px;font-weight:700;color:var(--teal-deep);text-transform:uppercase}
  .section-sub{position:absolute;left:300px;width:600px;text-align:center;font-size:15px;line-height:22px;color:var(--muted)}
  .feature{position:absolute;top:1210px;width:300px;text-align:center}
  .feature svg{display:block;margin:0 auto 14px}
  .feature h3{font-size:22px;font-weight:500;color:var(--teal-deep);margin-bottom:10px}
  .feature p{font-size:14px;line-height:20px;color:var(--muted);width:220px;margin:0 auto}

  /* how it works */
  .glow{position:absolute;border-radius:50%;background:var(--teal-glow)}
  .phone-steps{left:128px;top:1540px;width:272px;height:680px;background:linear-gradient(180deg,#3b3a33 0%,#274548 45%,#0d3338 100%)}
  .how-title{position:absolute;left:690px;top:1560px;font-size:34px;font-weight:500;color:var(--teal-deep);text-transform:uppercase}
  .steps-line{position:absolute;left:722px;top:1710px;width:2px;height:380px;background:var(--teal-soft)}
  .step{position:absolute;left:694px;width:420px;height:80px}
  .step-num{position:absolute;left:0;top:0;width:58px;height:58px;border-radius:50%;border:3px solid var(--teal-soft);background:var(--white);color:var(--teal-bright);font-size:24px;display:flex;align-items:center;justify-content:center}
  .step-num.active{background:var(--teal);color:var(--white)}
  .step h4{position:absolute;left:110px;top:-2px;font-size:21px;font-weight:500;color:var(--teal);white-space:nowrap}
  .step p{position:absolute;left:110px;top:30px;width:230px;font-size:14px;line-height:20px;color:var(--muted)}

  /* difference band */
  .band{position:absolute;left:0;top:2370px;width:1200px;height:410px;background:linear-gradient(180deg,var(--band-a),var(--band-b));color:var(--white)}
  .band .section-title{color:var(--white);top:88px}
  .band .section-sub{color:#cfe9ec;top:128px}
  .diff{position:absolute;top:238px;width:300px;text-align:center}
  .diff h3{font-size:22px;font-weight:500;margin-bottom:12px}
  .diff p{font-size:14px;line-height:20px;color:#d4eef0;width:220px;margin:0 auto}

  /* closing */
  .cta{position:absolute;left:0;top:2780px;width:1200px;height:390px;background:var(--night);color:var(--white)}
  .cta h2{position:absolute;left:0;top:180px;width:1200px;text-align:center;font-size:30px;font-weight:700;text-transform:uppercase}
  .cta p{position:absolute;left:330px;top:228px;width:540px;text-align:center;font-size:16px;line-height:24px;color:#cfe0e3}
  .footer{position:absolute;left:0;top:3170px;width:1200px;height:70px;background:var(--white);border-top:1px solid var(--line)}
  .footer small{position:absolute;left:112px;top:26px;font-size:13px;color:var(--ink)}
  .socials{position:absolute;right:112px;top:24px;display:flex;gap:18px}
  .socials span{width:22px;height:22px;border-radius:50%;background:var(--night)}
</style>
</head>
<body>

<header class="hero">
  <div class="hero-circle"></div>
  <div class="hero-ring"></div>
  <div class="brand">vemb</div>
  <h1 class="hero-title">Experience more of<br><span class="accent">the world around</span><br>you</h1>
  <p class="hero-lead">Designed for real life—discover what's around you and share moments beyond the screen.</p>
  <div class="btn-row" style="left:112px;top:518px">
    <a class="btn btn-dark" href="#">Download the app</a>
    <a class="btn btn-light" href="#">See how it works</a>
  </div>
  <div class="phone phone-hero" role="img" aria-label="Phone showing the app sign-in screen over a photo of friends outdoors"></div>
</header>

<section class="stats">
  <div class="stat" style="left:112px"><b>1,200</b><span>Users</span></div>
  <div class="stat" style="left:400px"><b>1,000+</b><span>Downloads</span></div>
  <div class="stat" style="left:752px"><b>500</b><span>Likes</span></div>
  <div class="stat" style="left:1042px"><b>800</b><span>5-Star Ratings</span></div>
</section>

<section class="features">
  <h2 class="section-title" style="top:1066px">What you can do with the app</h2>
  <p class="section-sub" style="top:1110px">Whether you're heading out with friends or looking for something new to do, the app helps you discover experiences around you and connect through real moments.</p>

  <div class="feature" style="left:150px">
    <svg width="60" height="60" viewBox="0 0 60 60" fill="none" stroke="#17808c" stroke-width="2.2" stroke-linecap="round">
      <circle cx="30" cy="26" r="22" opacity=".35"/><circle cx="30" cy="26" r="14" opacity=".6"/>
      <path d="M30 38c-6-7-9-11-9-15a9 9 0 0 1 18 0c0 4-3 8-9 15z"/><circle cx="30" cy="23" r="3"/>
    </svg>
    <h3>Discover Nearby</h3>
    <p>Lorem ipsum dolor sit amet, consectetur adipiscing elit, sed do eiusmod dolore magna aliqua.</p>
  </div>
  <div class="feature" style="left:450px">
    <svg width="60" height="60" viewBox="0 0 60 60" fill="none" stroke="#17808c" stroke-width="2.2" stroke-linecap="round">
      <circle cx="20" cy="20" r="7"/><circle cx="40" cy="20" r="7"/>
      <path d="M8 46c0-8 5-13 12-13s12 5 12 13M28 46c0-8 5-13 12-13s12 5 12 13"/>
    </svg>
    <h3>Connect Socially</h3>
    <p>Lorem ipsum dolor sit amet, consectetur adipiscing elit, sed do eiusmod dolore magna aliqua.</p>
  </div>
  <div class="feature" style="left:750px">
    <svg width="60" height="60" viewBox="0 0 60 60" fill="none" stroke="#17808c" stroke-width="2.2" stroke-linecap="round" stroke-linejoin="round">
      <circle cx="30" cy="30" r="14"/><path d="M26 23l10 7-10 7z"/>
      <path d="M12 16a22 22 0 0 0 0 28M48 16a22 22 0 0 1 0 28"/>
    </svg>
    <h3>Live Offline</h3>
    <p>Lorem ipsum dolor sit amet, consectetur adipiscing elit, sed do eiusmod dolore magna aliqua.</p>
  </div>
</section>

<section class="how">
  <div class="glow" style="left:-150px;top:1550px;width:780px;height:620px;opacity:.5"></div>
  <div class="glow" style="left:-50px;top:1610px;width:580px;height:500px;background:#d6f0f3;opacity:.6"></div>
  <div class="glow" style="left:60px;top:1690px;width:380px;height:340px;background:#c4e9ee;opacity:.7"></div>
  <div class="phone phone-steps" role="img" aria-label="Phone showing an app event screen over a photo of friends, with four menu tiles and a join button"></div>

  <h2 class="how-title">How it works</h2>
  <div class="steps-line"></div>
  <div class="step" style="top:1652px"><div class="step-num active">01</div><h4>Download the app</h4><p>Excepteur sint occaecat cupidatat mollit anim id est laborum.</p></div>
  <div class="step" style="top:1786px"><div class="step-num">02</div><h4>Set Up Quickly</h4><p>Excepteur sint occaecat cupidatat mollit anim id est laborum.</p></div>
  <div class="step" style="top:1920px"><div class="step-num">03</div><h4>Discover</h4><p>Excepteur sint occaecat cupidatat mollit anim id est laborum.</p></div>
  <div class="step" style="top:2060px"><div class="step-num">04</div><h4>Get Out and Enjoy</h4><p>Excepteur sint occaecat cupidatat mollit anim id est laborum.</p></div>
  <div class="btn-row" style="left:692px;top:2180px"><a class="btn btn-dark" href="#">Download the app</a></div>
</section>

<section class="band">
  <h2 class="section-title">What makes it different</h2>
  <p class="section-sub">Whether you're heading out with friends or looking for something new to do, the app helps you discover experiences around you and connect through real moments.</p>
  <div class="diff" style="left:110px"><h3>Instantly Familiar</h3><p>Lorem ipsum dolor sit amet, consectetur adipiscing elit, sed do eiusmod dolore magna aliqua.</p></div>
  <div class="diff" style="left:450px"><h3>Social by Design</h3><p>Lorem ipsum dolor sit amet, consectetur adipiscing elit, sed do eiusmod dolore magna aliqua.</p></div>
  <div class="diff" style="left:790px"><h3>Real-world First</h3><p>Lorem ipsum dolor sit amet, consectetur adipiscing elit, sed do eiusmod dolore magna aliqua.</p></div>
</section>

<section class="cta">
  <h2>Ready to experience it?</h2>
  <p>Download the app and start discovering nearby experiences, connecting with people, and spending more time in the real world.</p>
  <div class="btn-row" style="left:394px;top:310px">
    <a class="btn btn-dark" href="#">Download the app</a>
    <a class="btn btn-light" href="#">See how it works</a>
  </div>
</section>

<footer class="footer">
  <small>Copyright © 2026 Vemb. All rights reserved.</small>
  <div class="socials" aria-label="Social links"><span></span><span></span><span></span><span></span></div>
</footer>

</body>
</html>
```